依頼詳細
PCとスマホデザインの両方納品をいただきますが、
まずはデザインイメージが確認しやすいPCページのみの提案をお願いします。
スマホページは当選者に納品時にお願いしたいと思います。
スマホサイズについて、表示は横幅375pxで作成し、
デザインデータは2倍の横幅750pxのカンバスサイズで作成してください。
(Retinaディスプレイに対応するため)
レスポンシブウェブデザインを意識したデザインでお願いします。

■サイトマップ
添付の画面遷移図をご確認ください。

■参考サイト
https://www.kurumi-p.co.jp/
https://www.m-sorano.co.jp/
https://www.fujino-printing.co.jp/

■内容について
印刷会社のサイトリニューアルになります。
既存サイト
https://www.hinata-printing.co.jp/

■素材写真
画像データについては、フリー素材から流用して
イメージ画像に当て込んでください。
足りない場合は、一旦他のサイトの写真をサンプルとして
入れてください。(サンプルなどの表記をお願いします)
また、購入が必要な写真などを利用した場合、
価格とサイト名を教えてください。

また、Pixmora Stockで定期契約をしていますので、
Pixmora Stockの画像は使用できます。
デザイン時はカンプ画像をお入れいただきますようお願いします。

※採用サイト寄りのサイトにしたいので、使用する画像は
なるべく人物が入っているものを使用してください。

■ワイヤーフレーム
https://mock.plavetta.jp/view/51830427-216b-4c73-9a05-87162534907e-4182/?fullscreen
コンテンツの構成としてワイヤーフレームを作成しましたが
必ずしもワイヤーフレームの通りではなくて大丈夫です。
TOPページに配置するコンテンツを見ていただき、デザインは
デザイナーの皆様におまかせしたいと思います。

----------------------------------------------------------------------------
【制作物に対するお願い】

■フォントについて
・無料で使えるフォントで作成をお願いします。
・OSに紐づくフォントの使用は控えていただければと思います (ヒラギノなど)

ページ数
1ページ
希望イメージ
シンプル 複雑
単色 カラフル
暗い 明るい
日常 高級
遊び心 厳粛
未来的 伝統的
女性的 男性的
希望する色
青系、既存サイトに載っているロゴのイメージでお願いします。
納品ファイル
• 高解像度JPG (.jpg)
• イラストレーター形式 (.ai)
• フォトショップ形式 (.psd)
補足説明
上記のいずれか1つ(アウトラインありとなしの2つ)と高解像度JPGを納品お願いします。
adobe XDでの納品も可能です。

```html
<!DOCTYPE html>
<html lang="ja">
<head>
<meta charset="utf-8">
<title>ヒナタ印刷</title>
<link href="https://fonts.googleapis.com/css2?family=Montserrat:wght@600;700;800&family=Noto+Sans+JP:wght@400;500;700&display=swap" rel="stylesheet">
<style>
:root{
  --blue:#1f8fd6;
  --blue-dark:#1b6fb0;
  --heading:#2a8fd2;
  --ink:#333;
  --muted:#777;
  --pale:#eef7fc;
  --line:#d9d9d9;
  --footer:#4a4a4a;
  --white:#fff;
}
*{margin:0;padding:0;box-sizing:border-box}
html,body{width:1200px;height:4892px;overflow:hidden}
body{font-family:"Noto Sans JP",sans-serif;color:var(--ink);background:var(--white);position:relative}
.section{position:absolute;left:0;width:1200px}
.sec-title{text-align:center;font-family:"Montserrat",sans-serif;font-weight:800;font-size:48px;color:var(--heading);letter-spacing:2px;line-height:1}
.sec-sub{text-align:center;font-size:14px;color:var(--ink);margin-top:10px}
.btn-more{display:block;width:320px;height:64px;margin:0 auto;border-radius:32px;background:var(--white);box-shadow:0 3px 10px rgba(0,0,0,.15);text-align:center;line-height:64px;font-size:17px;font-weight:500;color:var(--ink);position:relative}
.btn-more::after{content:"";position:absolute;right:30px;top:28px;width:8px;height:8px;border-top:2px solid var(--ink);border-right:2px solid var(--ink);transform:rotate(45deg)}

/* header & hero */
.hero{top:0;height:720px;background:linear-gradient(135deg,#e9edf2 0%,#c9cdd4 35%,#8f97a4 60%,#c84a3c 80%,#d9dde2 100%)}
.hero-photo{position:absolute;inset:0;background:linear-gradient(160deg,rgba(240,242,246,.9),rgba(180,186,196,.6) 40%,rgba(200,80,60,.55) 75%,rgba(60,60,70,.5))}
.hero-veil{position:absolute;inset:0;background:rgba(0,0,0,.18)}
.header{position:absolute;top:0;left:0;width:1200px;height:90px;background:rgba(255,255,255,.92);display:flex;align-items:center;padding:0 30px 0 40px}
.logo{display:flex;align-items:center;gap:12px;font-weight:700;font-size:30px;color:var(--blue-dark)}
.logo-mark{width:26px;height:26px;background:var(--blue)}
.nav{margin-left:auto;display:flex;align-items:center;gap:38px;font-size:15px;font-weight:500}
.nav-contact{background:var(--blue);color:var(--white);padding:12px 26px;border-radius:6px}
.hero-copy{position:absolute;top:270px;width:100%;text-align:center;color:var(--white)}
.hero-copy h1{font-size:38px;font-weight:500;letter-spacing:3px;text-shadow:0 2px 8px rgba(0,0,0,.35)}
.hero-copy p{font-family:"Montserrat",sans-serif;font-weight:600;font-size:26px;margin-top:14px;text-shadow:0 2px 8px rgba(0,0,0,.35)}
.hero-btn{display:inline-block;margin-top:44px;width:340px;height:60px;line-height:60px;border-radius:30px;background:var(--blue);color:var(--white);font-size:17px}

/* about */
.about{top:720px;height:480px;padding-top:80px}
.about-lead{text-align:center;font-size:22px;font-weight:500;margin-top:36px}
.about-text{width:760px;margin:26px auto 0;text-align:center;font-size:14px;line-height:2.1;color:#555}

/* service */
.service{top:1200px;height:920px;background:var(--pale);padding-top:64px}
.service-intro{text-align:center;font-size:14px;line-height:2;color:#555;margin-top:26px}
.service-grid{display:grid;grid-template-columns:repeat(4,170px);justify-content:center;column-gap:88px;row-gap:36px;margin-top:40px}
.service-item{text-align:center;font-size:16px;font-weight:500}
.service-img{width:170px;height:170px;border-radius:50%;margin-bottom:16px}
.service .btn-more{margin-top:50px}

/* works */
.works{top:2120px;height:780px;padding-top:80px}
.works-list{display:flex;justify-content:center;gap:20px;margin-top:48px}
.work-card{width:280px;background:var(--white);box-shadow:0 2px 10px rgba(0,0,0,.12)}
.work-img{height:190px}
.work-body{padding:18px 20px 20px}
.work-body p{font-size:14px;font-weight:700;line-height:1.6}
.work-tag{display:inline-block;margin-top:14px;font-size:11px;color:var(--muted);background:#eee;padding:3px 10px}
.works .btn-more{margin-top:56px}

/* banners */
.banners{top:2900px;height:290px;background:var(--pale);display:flex;justify-content:center;gap:20px;padding-top:30px}
.banner{width:400px;height:220px;position:relative;display:flex;align-items:center;justify-content:flex-end;padding-right:36px}
.banner span{font-family:"Montserrat",sans-serif;font-weight:800;font-size:40px;color:var(--white);letter-spacing:2px;position:relative}
.banner-company{background:linear-gradient(120deg,#e6463c,#f2c14e 35%,#3c8ed8 65%,#9ad0f0)}
.banner-drafts{width:460px;background:linear-gradient(120deg,#f1e3c4,#e88b4a 30%,#5fb36a 55%,#4f8fd8 75%,#dfe5ea)}
.banner::before{content:"";position:absolute;inset:0;background:rgba(30,90,160,.25)}

/* news */
.news{top:3190px;height:790px;padding-top:110px}
.news-list{width:840px;margin:60px auto 0;list-style:none;border-top:1px solid var(--line)}
.news-item{display:flex;align-items:center;gap:24px;height:78px;border-bottom:1px solid var(--line);font-size:15px}
.news-date{font-family:"Montserrat",sans-serif;font-size:13px;color:var(--muted);width:90px}
.news-cat{font-size:12px;background:#eee;color:var(--muted);padding:4px 14px}
.news .btn-more{margin-top:62px}

/* blog */
.blog{top:3980px;height:520px;padding-top:40px}
.blog-list{display:flex;justify-content:center;gap:24px;margin-top:44px}
.blog-card{width:280px;background:var(--white);box-shadow:0 2px 10px rgba(0,0,0,.12)}
.blog-img{height:150px;background:linear-gradient(160deg,#8a8f98,#3f4650 60%,#c8ccd2)}
.blog-body{display:flex;align-items:center;gap:10px;padding:16px 18px;font-size:14px;font-weight:700}
.blog-icon{width:20px;height:20px;border-radius:50%;background:var(--blue);flex:none}
.blog .btn-more{margin-top:44px}

/* footer */
.footer{top:4500px;height:392px;background:var(--footer);color:#ddd;padding:50px 0 0 0}
.footer-inner{display:flex;width:900px;margin:0 auto}
.footer-info{width:420px;font-size:13px;line-height:1.9}
.footer .logo{color:var(--white);font-size:26px;margin-bottom:26px}
.footer-nav{display:grid;grid-template-columns:200px 200px;row-gap:14px;list-style:none;font-size:13px;margin-top:8px}
.copyright{position:absolute;bottom:22px;width:100%;text-align:center;font-size:11px;color:#aaa}
</style>
</head>
<body>

<section class="section hero">
  <div class="hero-photo" role="img" aria-label="印刷物の色見本を囲んで打ち合わせをする人々の手元の写真"></div>
  <div class="hero-veil"></div>
  <header class="header">
    <div class="logo"><span class="logo-mark"></span>ヒナタ印刷</div>
    <nav class="nav">
      <span>事業案内</span><span>入職について</span><span>事業紹介</span><span>会社概要</span>
      <span class="nav-contact">お問い合わせ</span>
    </nav>
  </header>
  <div class="hero-copy">
    <h1>共に考え、お客様のイメージをカタチにする</h1>
    <p>Thinking Together and Realizing Images</p>
    <span class="hero-btn">お問い合わせはこちら</span>
  </div>
</section>

<section class="section about">
  <h2 class="sec-title">ABOUT</h2>
  <p class="sec-sub">私たちについて</p>
  <p class="about-lead">ヒナタ印刷はお客様と共に考えます</p>
  <p class="about-text">
    新潟県の地域に根ざし、創業以来、印刷・写真製版・加工など幅広い事業を展開してまいりました。<br>
    商業印刷からパッケージ、販促ツールまで、お客様のご要望に合わせた提案を大切にしています。<br>
    時代とともに変わる情報の伝え方に寄り添い、デジタル分野にも積極的に取り組んでおります。<br>
    私たちは「何を伝えたいのか」を共に考え、最適なカタチにすることを使命としています。<br>
    一つひとつの仕事に真摯に向き合い、信頼される企業であり続けることを目指します。<br>
    これからも地域とお客様の未来のために、挑戦を続けてまいります。
  </p>
</section>

<section class="section service">
  <h2 class="sec-title">SERVICE</h2>
  <p class="sec-sub">事業内容</p>
  <p class="service-intro">ヒナタ印刷では、お客様の目的に合ったさまざまな印刷物を制作しております。<br>企画から納品まで、必要なツールを一貫してご提案いたします。</p>
  <div class="service-grid">
    <div class="service-item"><div class="service-img" role="img" aria-label="印刷機から流れる印刷物の写真" style="background:linear-gradient(135deg,#dfe4ea,#6f8fb0 55%,#2d3e55)"></div>一般商業印刷</div>
    <div class="service-item"><div class="service-img" role="img" aria-label="黒と白の紙箱パッケージの写真" style="background:linear-gradient(135deg,#f2f2f2,#9a9a9a 45%,#1e1e1e)"></div>パッケージ関連印刷</div>
    <div class="service-item"><div class="service-img" role="img" aria-label="店頭に並ぶ展示用ツールの写真" style="background:linear-gradient(135deg,#f4f4f4,#e0b0c0 40%,#8fc4d8 70%,#d8d8d8)"></div>展示・販促ツール</div>
    <div class="service-item"><div class="service-img" role="img" aria-label="色見本帳が広げられた写真" style="background:linear-gradient(135deg,#f4f4f4,#e85a4a 40%,#5ab870 60%,#4a88d8)"></div>オンデマンド印刷</div>
    <div class="service-item"><div class="service-img" role="img" aria-label="本棚に並ぶ書籍の写真" style="background:linear-gradient(135deg,#cfc2a8,#7a6048 50%,#3a4a5a)"></div>オンデマンド印刷</div>
    <div class="service-item"><div class="service-img" role="img" aria-label="タブレットで電子書籍を読む写真" style="background:linear-gradient(135deg,#f0f0f0,#b8b8b8 50%,#3a3a3a)"></div>WEB・電子書籍</div>
    <div class="service-item"><div class="service-img" role="img" aria-label="多言語の翻訳資料の写真" style="background:linear-gradient(135deg,#f6f6f6,#dcdcdc 50%,#a8a8a8)"></div>各種翻訳サービス</div>
  </div>
  <span class="btn-more">詳しく見る</span>
</section>

<section class="section works">
  <h2 class="sec-title">WORKS</h2>
  <p class="sec-sub">事例紹介</p>
  <div class="works-list">
    <article class="work-card"><div class="work-img" role="img" aria-label="資料を手にする人の手元の写真" style="background:linear-gradient(150deg,#e8ecf0,#aab4c0 50%,#7a8898)"></div><div class="work-body"><p>テキストが入ります。テキストが入ります。テキストが入ります。</p><span class="work-tag">会社名が入ります</span></div></article>
    <article class="work-card"><div class="work-img" role="img" aria-label="打ち合わせをする人々の写真" style="background:linear-gradient(150deg,#f0f0ee,#b8b0a4 50%,#6a6660)"></div><div class="work-body"><p>テキストが入ります。テキストが入ります。テキストが入ります。</p><span class="work-tag">会社名が入ります</span></div></article>
    <article class="work-card"><div class="work-img" role="img" aria-label="オフィスで話し合う社員の写真" style="background:linear-gradient(150deg,#eef0f2,#9aa6b4 50%,#505a68)"></div><div class="work-body"><p>テキストが入ります。テキストが入ります。テキストが入ります。</p><span class="work-tag">会社名が入ります</span></div></article>
  </div>
  <span class="btn-more">詳しく見る</span>
</section>

<section class="section banners">
  <div class="banner banner-company" role="img" aria-label="色とりどりの印刷物の写真"><span>COMPANY</span></div>
  <div class="banner banner-drafts" role="img" aria-label="扇状に広げた色見本の写真"><span>DRAFTS</span></div>
</section>

<section class="section news">
  <h2 class="sec-title">NEWS</h2>
  <p class="sec-sub">新着情報</p>
  <ul class="news-list">
    <li class="news-item"><span class="news-date">2022.06.20</span><span class="news-cat">お知らせ</span>ホームページをリニューアルしました。</li>
    <li class="news-item"><span class="news-date">2022.06.20</span><span class="news-cat">お知らせ</span>ホームページをリニューアルしました。</li>
    <li class="news-item"><span class="news-date">2022.06.20</span><span class="news-cat">お知らせ</span>ホームページをリニューアルしました。</li>
  </ul>
  <span class="btn-more">一覧を見る</span>
</section>

<section class="section blog">
  <h2 class="sec-title">BLOG</h2>
  <p class="sec-sub">ブログ</p>
  <div class="blog-list">
    <article class="blog-card"><div class="blog-img" role="img" aria-label="社員の集合写真"></div><div class="blog-body"><span class="blog-icon"></span>会長お招き例会</div></article>
    <article class="blog-card"><div class="blog-img" role="img" aria-label="会議室での報告会の写真"></div><div class="blog-body"><span class="blog-icon"></span>決算報告会開催</div></article>
    <article class="blog-card"><div class="blog-img" role="img" aria-label="新年会の集合写真"></div><div class="blog-body"><span class="blog-icon"></span>新年祝賀会</div></article>
  </div>
  <span class="btn-more">一覧を見る</span>
</section>

<footer class="section footer">
  <div class="footer-inner">
    <div class="footer-info">
      <div class="logo"><span class="logo-mark"></span>ヒナタ印刷</div>
      〒950-0000<br>新潟県○○市○○町1丁目2番3号<br>TEL：0120-48-7391（代表）<br>FAX：0120-48-7392
    </div>
    <ul class="footer-nav">
      <li>TOP</li><li>事業情報</li>
      <li>事業内容</li><li>ブログ</li>
      <li>事例紹介</li><li>お問い合わせ</li>
      <li>会社概要</li><li>プライバシーポリシー</li>
      <li>入職について</li><li>サイトポリシー</li>
    </ul>
  </div>
  <p class="copyright">Copyright © ヒナタ印刷 All Rights Reserved.</p>
</footer>

</body>
</html>
```